Flyer for Roadhaven 41Ter - Fresh Food Vending Machine in Helchteren

Project Description:
Roadhaven 41Ter has placed a new fresh food vending machine in Helchteren at KP Sodas (Lindeweg 517). We want to create an eye-catching, modern flyer to inform local residents about this vending machine and invite them to visit. The flyer will be distributed door-to-door in Helchteren.
Target Audience:
Residents of Helchteren and surrounding areas.
People looking for quick, fresh meals such as daily specials, wraps, poke bowls, soups, and pasta dishes.
Key Message:
Main title: "Helchteren, we’re here!"
Location: "Our brand-new fresh food vending machine is now at KP Sodas, Lindeweg 517!"
Available products: "Daily specials, wraps, poke bowls, soups, pasta dishes, and more."
Promotion: "For a limited time: with every product, you’ll receive a scratch card, and you always win!"
Style Guidelines:
Clean, professional, and inviting design.
Follow the new branding style of Roadhaven 41Ter (refer to the most recent posts on our Instagram and Facebook pages). Or see attachment for the layout inspiration.
Instagram: www.pictagram-example.com/roadhaven41ter
Facebook: www.friendbook-example.com/Roadhaven41
Do not use the older branding visible in earlier posts.
Format:
Flyer size: A5 (148 x 210 mm).
Additional Information:
Include our logos and social media accounts on the flyer.
Add a clear call-to-action, such as: "Visit us today!"
Ensure the flyer is easy to read and that all information is clear at a glance.
We look forward to seeing your creative and inspiring designs!

```html
<!DOCTYPE html>
<html lang="en">
<head>
<meta charset="utf-8">
<title>Roadhaven 41Ter – Helchteren flyer</title>
<link rel="stylesheet" href="https://fonts.googleapis.com/css2?family=Graduate&family=Lobster&family=Poppins:wght@500;600&display=swap">
<style>
  :root {
    --page-bg: #ffffff;
    --brand-blue: #0a5ec2;
    --brand-blue-deep: #064fa8;
    --brand-ice: #c9ddf3;
    --ink-blue: #1c5fc2;
    --white: #ffffff;
    --wrap-tone: #d9b48a;
    --poke-tone: #e9e4dc;
    --pasta-tone: #2c2a2a;
    --soup-tone: #e58a1f;
  }
  * { margin: 0; padding: 0; box-sizing: border-box; }
  html, body { width: 1200px; height: 2189px; overflow: hidden; background: var(--page-bg); }
  .flyer {
    position: absolute; left: 100px; top: 385px;
    width: 1000px; height: 1419px;
    background: linear-gradient(160deg, var(--brand-blue) 0%, var(--brand-blue-deep) 100%);
    overflow: hidden;
    font-family: "Poppins", sans-serif;
  }
  .brand-pill {
    position: absolute; left: 94px; top: 39px; width: 302px; height: 110px;
    background: var(--brand-ice); border-radius: 24px;
    display: flex; align-items: center; justify-content: center;
  }
  .brand-name {
    font-family: "Graduate", serif; font-size: 26px; color: var(--ink-blue);
    white-space: nowrap;
  }
  .machine-photo {
    position: absolute; left: 80px; top: 170px; width: 350px; height: 495px;
    border: 4px solid var(--brand-ice); border-radius: 34px;
    background: linear-gradient(180deg, #8b8f98 0%, #3b3f47 40%, #5a5e66 75%, #9ea3ab 100%);
  }
  .speech-bubble { position: absolute; left: 22px; top: 688px; width: 530px; height: 230px; }
  .headline {
    position: absolute; left: 22px; top: 718px; width: 475px;
    font-family: "Graduate", serif; color: var(--ink-blue);
    font-size: 58px; line-height: 68px; text-align: center;
  }
  .headline .highlight {
    background: var(--ink-blue); color: var(--white);
    border-radius: 12px; padding: 0 10px;
  }
  .promo-kicker {
    position: absolute; left: 40px; top: 950px; width: 430px; text-align: center;
    font-family: "Lobster", cursive; font-size: 50px; color: var(--brand-ice);
  }
  .kicker-rule { position: absolute; height: 2px; background: var(--brand-ice); top: 1000px; width: 126px; }
  .kicker-rule.left { left: 38px; }
  .kicker-rule.right { left: 346px; }
  .promo-title {
    position: absolute; left: 38px; top: 1010px; width: 434px; text-align: center;
    font-family: "Graduate", serif; font-size: 56px; color: var(--white);
    border-bottom: 2px solid var(--brand-ice); padding-bottom: 4px;
  }
  .promo-copy {
    position: absolute; left: 20px; top: 1096px; width: 470px; text-align: center;
    color: var(--white); font-size: 25px; font-weight: 600; line-height: 32px;
  }
  .promo-copy u { text-underline-offset: 4px; }
  .location {
    position: absolute; left: 20px; top: 1200px; width: 470px; text-align: center;
    color: var(--brand-ice); font-size: 19px; font-weight: 500;
  }
  .cta {
    position: absolute; left: 60px; top: 1250px; width: 387px; height: 58px;
    background: var(--white); border-radius: 30px;
    display: flex; align-items: center; justify-content: center;
    font-family: "Graduate", serif; font-size: 34px; color: var(--ink-blue);
  }
  .social { position: absolute; top: 1350px; display: flex; align-items: center; gap: 24px;
    color: var(--white); font-size: 23px; font-weight: 600; }
  .social.friendbook { left: 38px; }
  .social.pictagram { left: 332px; }
  .social .marker { width: 46px; height: 46px; border-radius: 12px; background: var(--brand-ice); opacity: .55; }
  .food { position: absolute; }
  .food.wrap {
    left: 505px; top: 25px; width: 520px; height: 360px; border-radius: 50%;
    transform: rotate(-28deg);
    background: radial-gradient(circle at 55% 50%, #f1ebe2 0%, var(--wrap-tone) 60%);
  }
  .food.poke {
    left: 620px; top: 422px; width: 400px; height: 400px; border-radius: 50%;
    background: radial-gradient(circle at 40% 45%, #b8424f 0%, var(--poke-tone) 55%, #ffffff 70%);
  }
  .food.pasta {
    left: 720px; top: 850px; width: 290px; height: 290px; border-radius: 50%;
    background: radial-gradient(circle, #c8644e 0%, #9a4a3a 55%, var(--pasta-tone) 62%);
  }
  .food.soup {
    left: 740px; top: 1150px; width: 268px; height: 268px; border-radius: 50%;
    background: radial-gradient(circle, var(--soup-tone) 0%, #d9791a 60%, #f4f1ec 64%);
  }
  .menu-label {
    position: absolute; font-family: "Graduate", serif; font-size: 44px;
    color: var(--white); white-space: nowrap; letter-spacing: 2px;
    transform: translate(-50%, -50%) rotate(var(--tilt));
  }
</style>
</head>
<body>
  <main class="flyer">
    <div class="brand-pill"><span class="brand-name">Roadhaven 41Ter</span></div>

    <div class="machine-photo" role="img" aria-label="Photo of the fresh food vending machine stocked with meals"></div>

    <svg class="speech-bubble" viewBox="0 0 530 230" aria-hidden="true">
      <path d="M40 0 H435 A40 40 0 0 1 475 40 V150 L530 170 L470 175 A45 45 0 0 1 430 230 H40 A40 40 0 0 1 0 190 V40 A40 40 0 0 1 40 0 Z" fill="var(--brand-ice)"/>
    </svg>
    <h1 class="headline">HELCHTEREN,<br>WE'RE <span class="highlight">HERE!</span></h1>

    <div class="kicker-rule left"></div>
    <div class="kicker-rule right"></div>
    <p class="promo-kicker">For a</p>
    <h2 class="promo-title">LIMITED TIME</h2>
    <p class="promo-copy">with every product,<br>you’ll receive a <u>scratch card,</u><br>and you <u>always win!</u></p>
    <p class="location">Now at KP Sodas, Lindeweg 517</p>
    <div class="cta">VISIT US TODAY!</div>

    <div class="social friendbook"><span class="marker"></span><span>Roadhaven41</span></div>
    <div class="social pictagram"><span class="marker"></span><span>roadhaven41ter</span></div>

    <div class="food wrap" role="img" aria-label="Wrap with salad on a wooden plate"></div>
    <div class="food poke" role="img" aria-label="Poke bowl with tuna, rice and cucumber"></div>
    <div class="food pasta" role="img" aria-label="Bowl of fusilli pasta"></div>
    <div class="food soup" role="img" aria-label="Bowl of orange soup with basil"></div>

    <span class="menu-label" style="left:506px;top:315px;--tilt:-80deg">WRAPS</span>
    <span class="menu-label" style="left:565px;top:630px;--tilt:-72deg">POKE BOWLS</span>
    <span class="menu-label" style="left:650px;top:1010px;--tilt:-72deg">PASTA</span>
    <span class="menu-label" style="left:692px;top:1276px;--tilt:-80deg">SOUPS</span>
  </main>
</body>
</html>
```